Soap Company Looking To Design New Soap Scent Boxes

we are looking to create a soap box similar to mr brindle. we would like the circle cut out on the top right corner of the box. we are looking for a design that will allow us to use different color base banners for different soap scents (like mr. brindle). we want the soap name scents to be large and readable on the bottom banner (like mr.brindle). we have included our brand figure (logo) and some previous older soap box designs that we were making before the brand figure. the box dims are attached.

```html
<!DOCTYPE html>
<html lang="en">
<head>
<meta charset="utf-8">
<title>Fern &amp; Tallow – Plumeria Soap Box</title>
<link href="https://fonts.googleapis.com/css2?family=Bowlby+One&family=Rubik:wght@500;700&display=swap" rel="stylesheet">
<style>
  :root {
    --page: #ffffff;
    --kraft: #e3d7c5;
    --kraft-edge: #d4c6b1;
    --ink: #2b1a12;
    --brand-accent: #f0a32a;
    --banner: #8a1a1d;
    --banner-text: #fbf3e6;
    --window-soap: #d9d2e0;
  }
  html, body {
    margin: 0;
    width: 1200px;
    height: 1200px;
    overflow: hidden;
    background: var(--page);
  }
  .canvas {
    position: relative;
    width: 1200px;
    height: 1200px;
  }
  .box-front {
    position: absolute;
    left: 220px;
    top: 220px;
    width: 760px;
    height: 760px;
    background: var(--kraft);
    box-shadow: inset 0 0 0 2px var(--kraft-edge);
    overflow: hidden;
  }
  .window-cutout {
    position: absolute;
    left: 600px;
    top: 33px;
    width: 120px;
    height: 120px;
    border-radius: 50%;
    background: var(--window-soap);
    box-shadow: inset 0 2px 6px rgba(0,0,0,0.25);
  }
  .brand {
    position: absolute;
    left: 0;
    right: 0;
    top: 50px;
    display: flex;
    flex-direction: column;
    align-items: center;
  }
  .brand-mark {
    width: 220px;
    height: 220px;
    border-radius: 50%;
    background: var(--brand-accent);
  }
  .brand-name {
    margin-top: 22px;
    font-family: "Bowlby One", sans-serif;
    font-size: 64px;
    line-height: 1;
    color: var(--ink);
    letter-spacing: 1px;
  }
  .scent-banner {
    position: absolute;
    left: 0;
    right: 0;
    bottom: 0;
    height: 262px;
    background: var(--banner);
    color: var(--banner-text);
    text-align: center;
  }
  .banner-rule {
    position: absolute;
    left: 0;
    right: 0;
    border-top: 3px dashed var(--banner-text);
  }
  .banner-rule.top { top: 16px; }
  .banner-rule.bottom { bottom: 16px; }
  .scent-name {
    margin: 46px 0 0;
    font-family: "Bowlby One", sans-serif;
    font-size: 92px;
    line-height: 1;
    letter-spacing: 4px;
  }
  .scent-type {
    margin: 14px 0 0;
    font-family: "Rubik", sans-serif;
    font-weight: 700;
    font-size: 25px;
    letter-spacing: 5px;
  }
  .net-weight {
    margin: 30px 0 0;
    font-family: "Rubik", sans-serif;
    font-weight: 500;
    font-size: 17px;
    letter-spacing: 0.5px;
  }
</style>
</head>
<body>
<main class="canvas">
  <section class="box-front">
    <div class="window-cutout" role="img" aria-label="Round window showing the lavender plumeria soap bar inside"></div>

    <div class="brand">
      <div class="brand-mark"></div>
      <div class="brand-name">Fern &amp; Tallow</div>
    </div>

    <div class="scent-banner">
      <div class="banner-rule top"></div>
      <h1 class="scent-name">PLUMERIA</h1>
      <p class="scent-type">COLD PRESSED ARTISAN SOAP</p>
      <p class="net-weight">NET WT.5oz(140g)</p>
      <div class="banner-rule bottom"></div>
    </div>
  </section>
</main>
</body>
</html>
```